Simple : A Therapist is looking for a Design

Im lookind for a business card design for my new business .
my therapy field - Attuned Somatic Release .
Its part of Osteopatic medicine .
its gental, not invasive method that focus on the bones of the skull (cranial) .
i want some kind of skull in it like the attached photo.

Target Market(s)

people that suffer from pain

Industry/Entity Type

Physical Therapy

Contact Information for Business Card

i want people to understand this is diffrent kind of therapy
its anatomy base , gental and give outstanding result .

Font styles to use
Serif

Colors
fee18a
cadf82
fbc994
cedeed
fbe7d2
fff3d1

Requirements
Must have
• one side: my name (Eliran Tsabari) ,
• phone number ( 0541762908)
• email (tsabarieliran@mailvent.net)
• other side : Attuned Somatic Release
Nice to have
• i want some kind of skull in it like the attached photo.
• very powrful, accurate and smart.
• nice colores (maybe lite orange?, lite green?) , simple, relax, smart

```html
<!DOCTYPE html>
<html lang="en">
<head>
<meta charset="utf-8">
<title>Eliran Tsabari – Business Card</title>
<link rel="stylesheet" href="https://fonts.googleapis.com/css2?family=Cinzel:wght@600&family=Open+Sans:wght@400&display=swap">
<style>
  :root {
    --backdrop: #262626;
    --card: #878787;
    --peach: #fbc994;
    --green: #cadf82;
    --white: #f4f4f4;
    --serif: "Cinzel", Georgia, serif;
    --sans: "Open Sans", Arial, sans-serif;
  }
  * { margin: 0; padding: 0; box-sizing: border-box; }
  html, body { width: 1200px; height: 895px; overflow: hidden; }
  body {
    background: var(--backdrop);
    display: flex;
    flex-direction: column;
    align-items: center;
    justify-content: center;
    gap: 36px;
  }
  .card {
    width: 690px;
    height: 394px;
    background: var(--card);
    box-shadow: 0 10px 30px rgba(0,0,0,.55);
    display: flex;
    align-items: center;
    justify-content: center;
  }
  .lockup { display: flex; align-items: center; gap: 22px; }
  .lockup__mark { width: 64px; height: 64px; background: var(--peach); flex: none; }
  .lockup__text { display: flex; flex-direction: column; }
  .lockup__name {
    font-family: var(--serif); color: var(--peach);
    font-size: 34px; font-weight: 600; line-height: 1.05; letter-spacing: .5px;
  }
  .lockup__field {
    font-family: var(--serif); color: var(--green);
    font-size: 31px; font-weight: 600; line-height: 1.15;
  }
  .lockup__tagline {
    font-family: var(--sans); color: var(--white);
    font-size: 17px; letter-spacing: 1px; margin-top: 4px;
  }
  .card--back { justify-content: space-between; padding: 0 44px 0 56px; }
  .card--back .lockup { gap: 14px; }
  .card--back .lockup__mark { width: 42px; height: 42px; }
  .card--back .lockup__name { font-size: 22px; }
  .card--back .lockup__field { font-size: 20px; }
  .card--back .lockup__tagline { font-size: 11px; }
  .divider { width: 2px; height: 130px; background: var(--white); }
  .contact { display: flex; flex-direction: column; gap: 8px; }
  .contact__name {
    font-family: var(--serif); color: var(--green);
    font-size: 26px; font-weight: 600; margin-bottom: 4px;
  }
  .contact__row {
    display: flex; align-items: center; gap: 12px;
    font-family: var(--sans); color: var(--white); font-size: 15px;
  }
  .contact__icon { width: 18px; height: 18px; flex: none; }
</style>
</head>
<body>
  <section class="card card--front">
    <div class="lockup">
      <span class="lockup__mark"></span>
      <div class="lockup__text">
        <span class="lockup__name">ELIRAN TSABARI</span>
        <span class="lockup__field">PHISIOTHERAPHY</span>
        <span class="lockup__tagline">ATTUNED SOMATIC RELEASE</span>
      </div>
    </div>
  </section>

  <section class="card card--back">
    <div class="lockup">
      <span class="lockup__mark"></span>
      <div class="lockup__text">
        <span class="lockup__name">ELIRAN TSABARI</span>
        <span class="lockup__field">PHISIOTHERAPHY</span>
        <span class="lockup__tagline">ATTUNED SOMATIC RELEASE</span>
      </div>
    </div>
    <span class="divider"></span>
    <div class="contact">
      <span class="contact__name">ELIRAN TSABARI</span>
      <span class="contact__row">
        <svg class="contact__icon" viewBox="0 0 24 24" aria-hidden="true"><path fill="#fbc994" d="M4 8c0-2 3-4 8-4s8 2 8 4v2h-4V8H8v2H4zm2 4h12l2 8H4zm6 2a2 2 0 100 4 2 2 0 000-4z"/></svg>
        0541762908
      </span>
      <span class="contact__row">
        <svg class="contact__icon" viewBox="0 0 24 24" aria-hidden="true"><path fill="#fbc994" d="M2 5h20v14H2zm2 2v.5l8 6 8-6V7zm0 3v7h16v-7l-8 6z"/></svg>
        tsabarieliran@mailvent.net
      </span>
    </div>
  </section>
</body>
</html>
```